Bright Harbor Realty

We need a good looking flyer for our real estate company to impress people who are considering to sell their homes for as low as 1.5% listing commission. Please see flyer examples for reference.
555-318-4096
Real Estate

```html
<!DOCTYPE html>
<html lang="en">
<head>
<meta charset="utf-8">
<title>Bright Harbor Realty – Just Sold Flyer</title>
<link rel="stylesheet" href="https://fonts.googleapis.com/css2?family=Open+Sans:wght@400;600;700;800&display=swap">
<style>
:root{
  --blue:#1f5aa8;
  --blue-dark:#17477f;
  --green:#2fa185;
  --red:#c8141c;
  --grey:#8a8a8c;
  --light:#eceef0;
  --ink:#2a2a2a;
  --page:#e6e7e9;
  --white:#ffffff;
}
*{box-sizing:border-box;margin:0;padding:0}
html,body{width:1200px;height:800px;overflow:hidden}
body{background:var(--page);font-family:"Open Sans",Arial,sans-serif;color:var(--ink);position:relative}
.card{position:absolute;background:var(--white);overflow:hidden;box-shadow:0 2px 8px rgba(0,0,0,.18)}
.abs{position:absolute}
.photo{position:absolute;overflow:hidden}
.ph-house{background:linear-gradient(180deg,#9cc6e8 0%,#b9cfa0 45%,#6f9a4e 100%)}
.ph-yellow{background:linear-gradient(180deg,#8fb86a 0%,#c9c07a 45%,#6c9444 100%)}
.ph-garage{background:linear-gradient(180deg,#a9cbe8 0%,#dedad0 50%,#8aa56a 100%)}
.ph-interior{background:linear-gradient(180deg,#d8d8d6 0%,#b9b7b2 55%,#6f6e6c 100%)}
.ph-tan{background:linear-gradient(180deg,#a8cde9 0%,#cdb597 50%,#8a8a7a 100%)}
.ph-portrait{background:linear-gradient(180deg,#d9dbde 0%,#9aa0a6 60%,#3a3f46 100%)}
.ribbon{position:absolute;right:-22px;top:10px;width:90px;background:var(--red);color:#fff;font-size:8px;font-weight:600;text-align:center;transform:rotate(45deg);line-height:13px}
.brand{font-weight:700;color:var(--blue);display:flex;align-items:center;gap:6px;line-height:1.1}
.brand i{display:block;width:12px;height:12px;background:var(--blue);flex:none}

/* front */
.front{left:96px;top:33px;width:474px;height:670px}
.side-bar{left:0;top:23px;width:20px;height:207px;background:var(--blue)}
.front .brand{left:310px;top:52px;width:150px;font-size:17px}
.sold-box{left:183px;top:141px;width:170px;height:113px;background:var(--blue);padding:5px}
.sold-frame{border:2px solid #fff;height:100%;color:#fff;text-align:center;display:flex;flex-direction:column;justify-content:center}
.sold-line1{font-size:44px;font-weight:400;line-height:44px;letter-spacing:1px}
.sold-line2{font-size:48px;font-weight:700;line-height:50px;letter-spacing:1px}
.grey-block{left:0;top:235px;width:74px;height:106px;background:var(--grey)}
.banner{left:0;top:347px;width:460px;height:57px}
.banner-text{left:20px;top:350px;color:#fff}
.banner-text h2{font-size:26px;font-weight:800;letter-spacing:.3px;line-height:30px}
.banner-text p{font-size:18px;line-height:22px}
.strip{left:4px;top:411px;width:466px;height:112px;background:var(--light)}
.mini{position:absolute;top:415px;width:150px}
.mini .photo{position:relative;height:79px}
.mini .cap{background:var(--blue);color:#fff;font-size:7.5px;text-align:center;line-height:10px;padding:3px 2px;height:24px}
.promo{left:8px;top:528px;width:329px;height:134px;background:var(--green);color:#fff;padding:5px 13px}
.promo h3{font-size:19px;font-weight:700;line-height:24px}
.promo p{font-size:9.5px;line-height:13px;margin-top:3px}
.promo p b{font-weight:700}
.promo h4{font-size:14px;font-weight:700;margin-top:7px;letter-spacing:.2px}
.promo .phone{display:flex;align-items:center;gap:8px;font-size:25px;font-weight:700;line-height:30px}
.promo .web{font-size:14px;margin-top:2px}
.socials{display:flex;gap:3px}
.socials span{width:11px;height:11px;border:1px solid currentColor;border-radius:50%}
.promo .socials{position:absolute;right:12px;bottom:13px}
.promo-edge{left:4px;top:662px;width:333px;height:5px;background:var(--blue)}
.agent-photo{left:344px;top:528px;width:119px;height:119px}
.agent-name{left:344px;top:647px;width:119px;height:17px;background:var(--blue);border:1px solid #fff;color:#fff;font-size:11px;font-weight:700;text-align:center;line-height:15px}

/* back */
.back{left:628px;top:31px;width:484px;height:682px}
.top-band{left:0;top:0;width:484px;height:6px;background:var(--green)}
.top-rule{left:0;top:11px;width:484px;height:2px;background:#333}
.touch{left:22px;top:35px;font-size:19px;color:var(--blue);padding:2px 0 0 6px;line-height:24px}
.back .brand{left:262px;top:52px;width:120px;font-size:12px}
.stamp{left:397px;top:27px;width:67px;height:62px;background:#e1e2e4}
.contact{left:22px;width:230px;display:flex;align-items:flex-start;gap:6px;color:var(--ink);white-space:nowrap}
.contact svg{flex:none;margin-top:2px}
.c-addr{top:101px;font-size:12.5px;line-height:17px}
.c-phone{top:138px;font-size:19px;font-weight:700;line-height:24px}
.c-web{top:168px;font-size:14px;line-height:19px}
.back .socials{left:24px;top:197px;color:var(--blue);gap:4px}
.back .socials span{width:13px;height:13px}
.addr-line{left:235px;width:229px;height:1px;background:#9a9a9a}
.msg-band{left:0;top:237px;width:484px;height:34px;background:var(--green);color:#fff;font-size:10.5px;font-weight:700;text-align:center;line-height:14px;padding-top:3px}
.msg-rule{left:0;top:274px;width:484px;height:2px;background:#444}
.row{position:absolute;left:0;width:484px;height:116px}
.row .photo{left:25px;top:0;width:198px;height:90px}
.row .cap{position:absolute;left:25px;top:90px;width:198px;height:28px;background:var(--blue);color:#fff;font-size:8px;text-align:center;line-height:11px;padding-top:3px}
.row .info{position:absolute;left:243px;top:0;width:225px}
.row .info::before{content:"";display:block;width:34px;height:3px;background:var(--blue);margin-bottom:1px}
.row h5{font-size:10.5px;font-weight:700;color:var(--blue);letter-spacing:.2px;line-height:14px}
.row ul{list-style:none;margin-top:4px}
.row li{font-size:8px;line-height:13.5px;display:flex;gap:9px;align-items:center}
.row .body{font-size:8px;line-height:11px;margin-top:3px}
.btns{position:absolute;left:245px;top:96px;display:flex;gap:4px}
.btns span{height:15px;color:#fff;font-size:10px;line-height:15px;padding-left:10px}
.btn-price{width:68px;background:var(--blue)}
.btn-time{width:86px;background:var(--green)}
.dots{left:25px;width:443px;border-top:2px dotted #444}
.bottom-rule{left:0;top:673px;width:484px;height:3px;background:var(--green)}
.bottom-rule2{left:0;top:678px;width:484px;height:2px;background:#333}
</style>
</head>
<body>

<section class="card front" aria-label="Flyer front">
  <div class="abs side-bar"></div>
  <div class="photo ph-yellow" style="left:24px;top:23px;width:271px;height:207px" role="img" aria-label="Photo of a sold single-storey home with garden"></div>
  <div class="abs brand"><i></i>Bright Harbor Realty</div>
  <div class="photo ph-house" style="left:302px;top:130px;width:172px;height:100px" role="img" aria-label="Photo of a sold ranch-style home"></div>
  <div class="abs grey-block"></div>
  <div class="photo ph-garage" style="left:81px;top:235px;width:214px;height:106px" role="img" aria-label="Photo of a sold home with carport"></div>
  <div class="photo ph-tan" style="left:302px;top:235px;width:172px;height:106px" role="img" aria-label="Photo of sold two-storey townhomes"></div>
  <div class="abs sold-box"><div class="sold-frame"><span class="sold-line1">JUST</span><span class="sold-line2">SOLD</span></div></div>

  <svg class="abs banner" width="460" height="57" viewBox="0 0 460 57">
    <polygon points="0,0 440,0 425,28 440,57 0,57" fill="#1f5aa8"/>
    <polyline points="432,6 448,30 432,54" fill="none" stroke="#8a8a8c" stroke-width="5"/>
  </svg>
  <div class="abs banner-text">
    <h2>LIST FOR 1.5% COMMISSION,</h2>
    <p>Still Receive Top Marketing!</p>
  </div>

  <div class="abs strip"></div>
  <div class="mini" style="left:8px">
    <div class="photo ph-house" role="img" aria-label="Photo of a listed two-storey home"><span class="ribbon">saved $3,750</span></div>
    <div class="cap">11820 Birchwood Circle Lakeview.<br>FL 33411 - $250,000</div>
  </div>
  <div class="mini" style="left:162px">
    <div class="photo ph-interior" role="img" aria-label="Photo of a listed home living room"><span class="ribbon">saved $5,443</span></div>
    <div class="cap">1540 E Meadowlark Drive Palm Ridge,<br>FL 33472 - $280,000</div>
  </div>
  <div class="mini" style="left:316px">
    <div class="photo ph-tan" role="img" aria-label="Photo of a listed two-storey home"><span class="ribbon">saved $3,350</span></div>
    <div class="cap">13655 Saltmarsh Circle Lakeview,<br>FL 33411 - $335,000</div>
  </div>

  <div class="abs promo">
    <h3>Did You Know?</h3>
    <p>On average, our customers save <b>$8, 750</b> when they choose us... and they still receive top marketing, servke and representation!</p>
    <h4>CALL US TODAY AND SAVE THOUSANDS</h4>
    <div class="phone">
      <svg width="20" height="20" viewBox="0 0 24 24"><path d="M6.6 10.8a15 15 0 0 0 6.6 6.6l2.2-2.2c.3-.3.7-.4 1-.2 1.1.4 2.3.6 3.6.6.6 0 1 .4 1 1V20c0 .6-.4 1-1 1A17 17 0 0 1 3 4c0-.6.4-1 1-1h3.5c.6 0 1 .4 1 1 0 1.3.2 2.5.6 3.6.1.3 0 .7-.2 1z" fill="#fff"/></svg>
      555-318-4096
    </div>
    <div class="web">www.website.com</div>
    <div class="socials"><span></span><span></span><span></span><span></span><span></span><span></span></div>
  </div>
  <div class="abs promo-edge"></div>
  <div class="photo ph-portrait agent-photo" role="img" aria-label="Portrait of the listing agent in a suit"></div>
  <div class="abs agent-name">MARCUS DELANEY</div>
</section>

<section class="card back" aria-label="Flyer back">
  <div class="abs top-band"></div>
  <div class="abs top-rule"></div>

  <div class="abs touch">
    <svg class="abs" style="left:0;top:0" width="152" height="28" viewBox="0 0 152 28"><polyline points="2,26 2,2 150,2 150,18" fill="none" stroke="#333" stroke-width="1.5"/></svg>
    Get In Touch
  </div>
  <div class="abs brand"><i></i>Bright Harbor Realty</div>
  <div class="abs stamp"></div>

  <div class="abs contact c-addr">
    <svg width="12" height="14" viewBox="0 0 12 14"><path d="M6 1a4.5 4.5 0 0 0-4.5 4.5C1.5 9 6 13 6 13s4.5-4 4.5-7.5A4.5 4.5 0 0 0 6 1z" fill="none" stroke="#333" stroke-width="1.4"/><circle cx="6" cy="5.5" r="1.6" fill="#333"/></svg>
    <span>Dana R. Whitcomb 482 Maple Grove<br>Circle Seabrook, FL 33218</span>
  </div>
  <div class="abs contact c-phone">
    <svg width="13" height="13" viewBox="0 0 24 24" style="margin-top:6px"><circle cx="12" cy="12" r="11" fill="none" stroke="#333" stroke-width="2"/><path d="M8 9.5a9 9 0 0 0 6.5 6.5l1.4-1.4c.2-.2.4-.2.6-.1l2 .8v1.9A8.5 8.5 0 0 1 6.8 5.5H8.8l.7 2c.1.2 0 .4-.1.6z" fill="#333"/></svg>
    <span>555-318-4096</span>
  </div>
  <div class="abs contact c-web">
    <svg width="13" height="13" viewBox="0 0 24 24" style="margin-top:3px"><circle cx="12" cy="12" r="11" fill="none" stroke="#333" stroke-width="2"/><path d="M1 12h22M12 1c4 4 4 18 0 22M12 1c-4 4-4 18 0 22" fill="none" stroke="#333" stroke-width="1.6"/></svg>
    <span>www.<b>website</b>.com</span>
  </div>
  <div class="abs socials"><span></span><span></span><span></span><span></span><span></span><span></span></div>

  <div class="abs addr-line" style="top:163px"></div>
  <div class="abs addr-line" style="top:188px"></div>
  <div class="abs addr-line" style="top:213px"></div>

  <div class="abs msg-band">Lorem ipsum dolor sit amet, consectetur adipiscing elit.<br>Morbi eu sem felis. Integer faucibus ligula vitae enim vestibulum iaculis.</div>
  <div class="abs msg-rule"></div>

  <div class="row" style="top:286px">
    <div class="photo ph-house" role="img" aria-label="Photo of a listed two-storey home"><span class="ribbon">Saved $4,200</span></div>
    <div class="cap">627 S Harbor Club Drive Bayport,<br>FL 33460-<b>$550,000</b></div>
    <div class="info">
      <h5>LOREM IPSUM DOLOR SIT AMET</h5>
      <ul>
        <li><svg width="8" height="7" viewBox="0 0 8 7"><path d="M1 3.5l2 2L7 1" fill="none" stroke="#333" stroke-width="1.3"/></svg>Quis Molestie Turpis Dapibus At</li>
        <li><svg width="8" height="7" viewBox="0 0 8 7"><path d="M1 3.5l2 2L7 1" fill="none" stroke="#333" stroke-width="1.3"/></svg>Quis Molestie Turpis Dapibus At</li>
        <li><svg width="8" height="7" viewBox="0 0 8 7"><path d="M1 3.5l2 2L7 1" fill="none" stroke="#333" stroke-width="1.3"/></svg>Quis Molestie Turpis Dapibus At</li>
      </ul>
      <p class="body">Lorem ipsum dolor sit amet, consectetur adipiscing elit. Praesent rhoncus nibh nisl</p>
    </div>
    <div class="btns"><span class="btn-price">PRICE</span><span class="btn-time">TIMEFRAME</span></div>
  </div>
  <div class="abs dots" style="top:407px"></div>

  <div class="row" style="top:417px">
    <div class="photo ph-interior" role="img" aria-label="Photo of a listed home living room"><span class="ribbon">Saved $4,200</span></div>
    <div class="cap">2190 Compass Circle E Sandpoint Beach,<br>FL 33440-<b>$229,500</b></div>
    <div class="info">
      <h5>CONSECTETUR ADIPISCING ELIT</h5>
      <ul>
        <li><svg width="8" height="7" viewBox="0 0 8 7"><path d="M1 3.5l2 2L7 1" fill="none" stroke="#2fa185" stroke-width="1.3"/></svg>Quis Molestie Turpis Dapibus At</li>
        <li><svg width="8" height="7" viewBox="0 0 8 7"><path d="M1 3.5l2 2L7 1" fill="none" stroke="#2fa185" stroke-width="1.3"/></svg>Quis Molestie Turpis Dapibus At</li>
        <li><svg width="8" height="7" viewBox="0 0 8 7"><path d="M1 3.5l2 2L7 1" fill="none" stroke="#2fa185" stroke-width="1.3"/></svg>Quis Molestie Turpis Dapibus At</li>
      </ul>
      <p class="body">Maecenas consectetur leo ex, eget rutrum eros volutpat non.Nulla in tellus eu lacus tempor</p>
    </div>
    <div class="btns"><span class="btn-price">PRICE</span><span class="btn-time">TIMEFRAME</span></div>
  </div>
  <div class="abs dots" style="top:541px"></div>

  <div class="row" style="top:551px">
    <div class="photo ph-tan" role="img" aria-label="Photo of a listed two-storey home"><span class="ribbon">Saved $5,250</span></div>
    <div class="cap">627 S Harbor Club Drive Bayport,<br>FL 33460-<b>$550,000</b></div>
    <div class="info">
      <h5>PRAESENT RHONCUS NIBH NISL</h5>
      <ul>
        <li><svg width="8" height="7" viewBox="0 0 8 7"><path d="M1 3.5l2 2L7 1" fill="none" stroke="#2fa185" stroke-width="1.3"/></svg>Quis Molestie Turpis Dapibus At</li>
        <li><svg width="8" height="7" viewBox="0 0 8 7"><path d="M1 3.5l2 2L7 1" fill="none" stroke="#2fa185" stroke-width="1.3"/></svg>Quis Molestie Turpis Dapibus At</li>
        <li><svg width="8" height="7" viewBox="0 0 8 7"><path d="M1 3.5l2 2L7 1" fill="none" stroke="#2fa185" stroke-width="1.3"/></svg>Quis Molestie Turpis Dapibus At</li>
      </ul>
      <p class="body">Maecenas consectetur leo ex, eget rutrum eros volutpat non.Nulla in tellus eu lacus tempor</p>
    </div>
    <div class="btns"><span class="btn-price">PRICE</span><span class="btn-time">TIMEFRAME</span></div>
  </div>

  <div class="abs bottom-rule"></div>
  <div class="abs bottom-rule2"></div>
</section>

</body>
</html>
```